Electrical Wholesaler Needs a New Website

Looking for a new website to be built for an electrical wholesaler based in Birmingham(England). Our logo is based on two Lions with a shield, so ideally the site should be deigned around that.

Looking for something that shows off our logo and incorporates what we are trying to do, preferably to have a colour scheme that is green and black if possible.

Target Market(s)

I'm looking for a professional website for my company that doesn't just look like amother WordPress template that I could build myself.

Industry/Entity Type

Electrical

Font styles to use
Sans Serif

Colors
9bcb3c
cadf82

Requirements
Must have
• Website with 4-5 pages, home page, about us, suppliers list, catalogue download and contact us. Search for UK electrical wholesalers to give you an idea of what I mean.

```html
<!DOCTYPE html>
<html lang="en">
<head>
<meta charset="utf-8">
<title>Stagford Electrical Wholesalers</title>
<link rel="stylesheet" href="https://fonts.googleapis.com/css2?family=Roboto+Condensed:wght@400;700&family=Roboto:wght@300;400&display=swap">
<style>
:root{
  --page-bg:#e6e6e6;
  --panel:#ffffff;
  --frame:#b3b3b3;
  --green-dark:#1d4a2c;
  --green:#9bcb3c;
  --green-mid:#6fa834;
  --green-soft:#cadf82;
  --text:#2b2b2b;
  --muted:#8a8a8a;
  --grey-logo:#6d6d6d;
}
*{box-sizing:border-box;margin:0;padding:0}
html,body{width:1121px;height:1200px;overflow:hidden}
body{background:var(--page-bg);font-family:'Roboto',sans-serif;color:var(--text);position:relative}
.abs{position:absolute}
.frame{position:absolute;left:0;top:0}
.crest-deco{position:absolute;top:0;width:153px;height:255px;background:radial-gradient(ellipse at center,#d4d4d4 0%,#dedede 55%,rgba(230,230,230,0) 75%)}
.crest-left{left:0}
.crest-right{right:0}
.cond{font-family:'Roboto Condensed',sans-serif}
.phone-top{left:806px;top:50px;width:137px;display:flex;align-items:center;gap:5px;color:var(--green);font-family:'Roboto Condensed',sans-serif;font-size:20px;font-weight:700}
.nav-link{top:104px;height:21px;border-bottom:2px solid var(--green-dark);color:var(--green-dark);font-family:'Roboto Condensed',sans-serif;font-weight:700;font-size:15.5px;line-height:19px}
.nav-right{text-align:right}
.brand{left:508px;top:58px;width:105px;text-align:center;color:var(--green-dark);font-family:'Roboto Condensed',sans-serif;font-weight:700;line-height:1}
.brand-name{font-size:24px;letter-spacing:.5px}
.brand-sub{font-size:7px;margin-top:4px;letter-spacing:.2px}
.brand-mark{width:22px;height:22px;border-radius:50%;background:var(--green);margin:0 auto 6px}
.hero{left:153px;top:146px;width:816px;height:340px;background:linear-gradient(100deg,#3b4660 0%,#5b5f6a 25%,#8c7f74 45%,#a33a36 62%,#6b5a50 80%,#c43a32 100%)}
.hero-caption{left:178px;top:274px;width:357px;height:183px;background:rgba(0,0,0,.72);padding:18px 13px}
.hero-title{color:var(--green);font-family:'Roboto Condensed',sans-serif;font-weight:700;font-size:20.5px;line-height:24px}
.hero-text{color:#fff;font-weight:300;font-size:13.4px;line-height:19.5px;margin-top:8px}
.btn{position:absolute;display:flex;align-items:center;justify-content:center;gap:5px;font-family:'Roboto Condensed',sans-serif;font-weight:700;border-radius:5px}
.btn-green{background:linear-gradient(#8cc34a,#4d8c2c);color:#fff;border:1px solid #4a7f2a}
.btn-grey{background:linear-gradient(#fafafa,#dedede);color:#6a6a6a;border:1px solid #b8b8b8;font-size:12px}
.hero-btn{left:191px;top:398px;width:141px;height:37px;font-size:15.5px}
.dots{left:910px;top:470px;display:flex;gap:4px}
.dot{width:8px;height:8px;border-radius:50%;background:#fff}
.dot.on{background:var(--green)}
.section-title{position:absolute;color:var(--green-dark);font-family:'Roboto Condensed',sans-serif;font-weight:700;font-size:19px;line-height:22px;border-bottom:1px solid var(--green-dark)}
.section-title span{display:inline-block;border-bottom:2px solid var(--green-dark);padding-bottom:3px;margin-bottom:-1px}
.why-list{left:170px;top:562px;width:238px;list-style:none}
.why-list li{display:flex;align-items:center;gap:7px;font-size:12px;height:23.8px;font-weight:300;color:#222}
.products-text{left:442px;top:561px;width:112px;font-size:12px;line-height:17px;font-weight:300;color:#222}
.catalogue-cover{left:573px;top:563px;width:107px;height:103px;background:linear-gradient(110deg,#2d2d2d 0%,#6c5a3f 25%,#1f5aa6 45%,#3c7bd0 70%,#e9eef6 100%);border:1px solid #ccc}
.field{position:absolute;left:714px;width:238px;border:1px solid #333;background:#fff;font-size:10px;font-style:italic;font-weight:300;color:#444;padding:6px 8px}
.supplier-row{left:170px;top:826px;width:782px;display:flex;justify-content:space-between;align-items:center;color:var(--grey-logo);font-family:'Roboto Condensed',sans-serif;font-weight:700}
.footer-brand{left:508px;top:950px}
.footer-links{left:0;width:1121px;top:1042px;text-align:center;font-family:'Roboto Condensed',sans-serif;font-weight:700;font-size:11.5px;color:#111}
.footer-links .sep{margin:0 7px;font-weight:400}
.footer-line{left:0;width:1121px;text-align:center;font-family:'Roboto Condensed',sans-serif;font-weight:700;font-size:11.5px;color:#111;display:flex;justify-content:center;align-items:center;gap:4px}
.social{left:538px;top:1100px;display:flex;gap:4px}
.social span{width:13px;height:13px;display:block}
.copyright{left:0;width:1121px;top:1152px;text-align:center;font-family:'Roboto Condensed',sans-serif;font-size:10px;color:var(--muted)}
</style>
</head>
<body>

<div class="crest-deco crest-left" role="img" aria-label="Faint heraldic crest decoration"></div>
<div class="crest-deco crest-right" role="img" aria-label="Faint heraldic crest decoration"></div>

<svg class="frame" width="1121" height="1200" viewBox="0 0 1121 1200" aria-hidden="true">
  <defs>
    <linearGradient id="panelFill" x1="0" y1="0" x2="0" y2="1">
      <stop offset="0" stop-color="#f2f2f2"/>
      <stop offset=".1" stop-color="#ffffff"/>
      <stop offset=".82" stop-color="#ffffff"/>
      <stop offset="1" stop-color="#ececec"/>
    </linearGradient>
  </defs>
  <path d="M151 39 H971 V892 C971 1000 720 1095 560 1139 C400 1095 151 1000 151 892 Z" fill="url(#panelFill)" stroke="#b3b3b3" stroke-width="4"/>
</svg>

<header>
  <div class="abs phone-top">
    <svg width="22" height="22" viewBox="0 0 22 22" aria-hidden="true"><circle cx="11" cy="11" r="10" fill="#9bcb3c" stroke="#6fa834"/><rect x="6" y="6" width="10" height="3" rx="1" fill="#fff"/><rect x="6" y="10" width="10" height="6" rx="1" fill="#fff"/></svg>
    121 555 0142
  </div>
  <nav>
    <a class="abs nav-link nav-right" style="left:187px;width:136px">ABOUT US</a>
    <a class="abs nav-link nav-right" style="left:348px;width:145px">SUPPLIERS</a>
    <a class="abs nav-link" style="left:629px;width:144px">CATALOGUE</a>
    <a class="abs nav-link" style="left:799px;width:144px">CONTACT US</a>
  </nav>
  <div class="abs brand">
    <div class="brand-mark"></div>
    <div class="brand-name">STAGFORD</div>
    <div class="brand-sub">ELECTRICAL WHOLESALERS</div>
  </div>
</header>

<section class="abs hero" role="img" aria-label="Photo of the trade counter with shelves of electrical stock"></section>
<div class="abs hero-caption">
  <h1 class="hero-title">Stagford Electrical Wholesalers</h1>
  <p class="hero-text">Lorem ipsum dolor sit amet, consectetur adipiscing elit. Aenean ullamcorper feugiat molestie. Aenean lacinia erat arcu. Cras condimentum turpis ac ante auctorp.</p>
</div>
<a class="btn btn-green hero-btn">CONTACT US <svg width="9" height="10" viewBox="0 0 9 10"><path d="M2 1l4 4-4 4" stroke="#fff" stroke-width="2" fill="none"/></svg></a>
<div class="abs dots"><span class="dot on"></span><span class="dot"></span><span class="dot"></span><span class="dot"></span></div>

<h2 class="section-title" style="left:170px;top:521px;width:238px"><span>WHY US?</span></h2>
<ul class="abs why-list">
  <li><svg width="14" height="16" viewBox="0 0 14 16"><path d="M7 0l7 2v6c0 4-3 7-7 8-4-1-7-4-7-8V2z" fill="#6fa834"/><path d="M3.5 8l2.5 2.5 4.5-5" stroke="#fff" stroke-width="1.8" fill="none"/></svg>Pellentesque dapibus nisi eget laoreet</li>
  <li><svg width="14" height="16" viewBox="0 0 14 16"><path d="M7 0l7 2v6c0 4-3 7-7 8-4-1-7-4-7-8V2z" fill="#6fa834"/><path d="M3.5 8l2.5 2.5 4.5-5" stroke="#fff" stroke-width="1.8" fill="none"/></svg>Volutpat est nulla rutrum enim eget cong</li>
  <li><svg width="14" height="16" viewBox="0 0 14 16"><path d="M7 0l7 2v6c0 4-3 7-7 8-4-1-7-4-7-8V2z" fill="#6fa834"/><path d="M3.5 8l2.5 2.5 4.5-5" stroke="#fff" stroke-width="1.8" fill="none"/></svg>In ut dui risus vestibulum id ligula olutpat</li>
  <li><svg width="14" height="16" viewBox="0 0 14 16"><path d="M7 0l7 2v6c0 4-3 7-7 8-4-1-7-4-7-8V2z" fill="#6fa834"/><path d="M3.5 8l2.5 2.5 4.5-5" stroke="#fff" stroke-width="1.8" fill="none"/></svg>Tempor lorem curabitur augue felis</li>
  <li><svg width="14" height="16" viewBox="0 0 14 16"><path d="M7 0l7 2v6c0 4-3 7-7 8-4-1-7-4-7-8V2z" fill="#6fa834"/><path d="M3.5 8l2.5 2.5 4.5-5" stroke="#fff" stroke-width="1.8" fill="none"/></svg>Diam lacinia consequat dapibus purus</li>
</ul>
<a class="btn btn-grey" style="left:308px;top:695px;width:100px;height:30px">LEARN MORE <svg width="8" height="10" viewBox="0 0 8 10"><path d="M2 1l4 4-4 4" stroke="#6a6a6a" stroke-width="2" fill="none"/></svg></a>

<h2 class="section-title" style="left:442px;top:521px;width:238px"><span>PRODUCTS</span></h2>
<p class="abs products-text">Curabitur lacinia imperdiet mauris, ut cursus enim. Nam venenatis leo libero, sed egestas velit imperdiet in gurabitur eget placerat dolor.</p>
<div class="abs catalogue-cover" role="img" aria-label="Product catalogue cover"></div>
<a class="btn btn-grey" style="left:552px;top:695px;width:128px;height:30px">VIEW CATALOGUES <svg width="8" height="10" viewBox="0 0 8 10"><path d="M2 1l4 4-4 4" stroke="#6a6a6a" stroke-width="2" fill="none"/></svg></a>

<h2 class="section-title" style="left:714px;top:521px;width:238px"><span>GET A QUOTE</span></h2>
<div class="field" style="top:563px;height:26px">Name</div>
<div class="field" style="top:593px;height:26px">Email</div>
<div class="field" style="top:623px;height:64px">Message</div>
<a class="btn btn-green" style="left:851px;top:695px;width:101px;height:30px;font-size:12px">GET A QUOTE <svg width="8" height="10" viewBox="0 0 8 10"><path d="M2 1l4 4-4 4" stroke="#fff" stroke-width="2" fill="none"/></svg></a>

<h2 class="section-title" style="left:170px;top:785px;width:782px"><span>FEATURED SUPPLIERS</span></h2>
<div class="abs supplier-row">
  <span style="font-size:19px">Hollybrook</span>
  <span style="font-size:12px;line-height:12px;text-align:center">KESTREL<br>TRUNKING</span>
  <span style="font-size:19px">Warmline</span>
  <span style="font-size:16px">TOOLCRAFT</span>
  <span style="font-size:20px">LUMARA</span>
  <span style="font-size:13px">NORVANE</span>
  <span style="font-size:20px">Precisa</span>
</div>
<a class="btn btn-grey" style="left:813px;top:866px;width:139px;height:30px">VIEW ALL SUPPLIERS <svg width="8" height="10" viewBox="0 0 8 10"><path d="M2 1l4 4-4 4" stroke="#6a6a6a" stroke-width="2" fill="none"/></svg></a>

<footer>
  <div class="abs brand footer-brand">
    <div class="brand-mark"></div>
    <div class="brand-name">STAGFORD</div>
    <div class="brand-sub">ELECTRICAL WHOLESALERS</div>
  </div>
  <nav class="abs footer-links">HOME<span class="sep">|</span>ABOUT US<span class="sep">|</span>SUPPLIERS<span class="sep">|</span>CATALOGUE<span class="sep">|</span>CONTACT US</nav>
  <div class="abs footer-line" style="top:1060px">
    <svg width="12" height="11" viewBox="0 0 12 11" aria-hidden="true"><rect x="0" y="0" width="12" height="3" fill="#111"/><rect x="1" y="4" width="10" height="7" fill="#111"/><rect x="3" y="6" width="2" height="1.5" fill="#fff"/><rect x="7" y="6" width="2" height="1.5" fill="#fff"/><rect x="3" y="8.5" width="2" height="1.5" fill="#fff"/><rect x="7" y="8.5" width="2" height="1.5" fill="#fff"/></svg>
    121 555 0142
  </div>
  <div class="abs footer-line" style="top:1079px">
    <svg width="13" height="9" viewBox="0 0 13 9" aria-hidden="true"><rect x="0.5" y="0.5" width="12" height="8" fill="#111"/><path d="M0.5 0.5l6 4.5 6-4.5" stroke="#fff" fill="none"/></svg>
    info@StagfordElectrical.com
  </div>
  <div class="abs social"><span style="background:#3b5998"></span><span style="background:#4aa3df"></span><span style="background:#d34836"></span></div>
  <p class="abs copyright">©2013 Stagford Electrical Wholesalers.</p>
</footer>

</body>
</html>
```